Logo and label design for our product coffee scrub

We need a logo design and a packaging label design for our new brand called "Rocco Velvetine". Best design wins 500$

It's a cosmetic brand with initial product "coffee scrub", which is a body peeling made of coffee, himalayan salt and additives. Brand will target young to middle aged women, who we will address with a very sexy and slightly provocative appeal (pictures of women wearing nothing but our coffee scrub - sample attached). Purpose of the coffee scrub is to target cellulite, stretch marks, psoriasis, varicose veins, eczema and acne.

Packaging that we will use will be a brown stand up pouch (attached) with a dimensions width 13cm, height 22cm and with a front and back sticker (dimensions width 7cm, height 14cm, round corners) or sticker that overlaps from front to back.

Looking forward on receiving your ideas!

Target Market(s)

Brand will targeting young to middle aged european women, who we will address with a very sexy and slightly provocative appeal (pictures of women wearing nothing but our coffee scrub - sample attached)

Industry/Entity Type

Product

Requirements
Must have
• Just an idea for the logo writing to use a handwriting font "Rocco Velvetine".

For the front side of packaging label you could use a picture of a women's body wearing a coffee scrub. Label should be very sexy but not vulgar.
Nice to have
• The back side of the label should have a cheesy pick up line and declaration text (just a sample):

hi babe! so you wanna get dirty! just show me the way to your bath. but first let me give you a proper introduction of myself. my name is rocco and i'm a coffee scrub wearing nothing but 250g of finest arabic coffee and sweet orange flavour & lots of other good stuff.

by the way I will help you with cellulite, stretch marks, psoriasis, varicose veins, eczema and acne. i’ll smooth your lumps and bumps with brown sugar & sea salt, moisturise and tone your skin with cold pressed sweet almond oil, and use vitamins & minerals to work wonders from the outside in. then i’ll make us both smell good with a little orange essence.

ingredients:
Coffea Robusta Seed Powder (Coffee), Prunus Amygdalus Dulcis (Sweet Almond) Oil, Water (Aqua), Sodium Chloride (Salt), Sucrose (Brown Sugar). All ingredients organic.

net weight: 200 g

best before date:

barcode

```html
<!DOCTYPE html>
<html lang="en">
<head>
<meta charset="utf-8">
<title>Rocco Velvetine – Coffee Scrub Label</title>
<link rel="stylesheet" href="https://fonts.googleapis.com/css2?family=Dancing+Script:wght@700&family=Oswald:wght@300;400&family=Special+Elite&display=swap">
<style>
  :root {
    --page: #ffffff;
    --label-light: #e6e6e8;
    --label-mid: #cfcfd3;
    --bean-dark: #2a1309;
    --bean-mid: #5a2c14;
    --bean-warm: #8a4a22;
    --ink: #2b2b2b;
    --brand-brown: #3d2414;
    --skin-light: #c98a62;
    --skin-dark: #5e3420;
    --rule: #8d8d92;
  }
  html, body {
    margin: 0;
    width: 1200px;
    height: 900px;
    overflow: hidden;
    background: var(--page);
  }
  .label {
    position: absolute;
    left: 410px;
    top: 50px;
    width: 390px;
    height: 780px;
    border-radius: 18px;
    overflow: hidden;
    background: radial-gradient(ellipse at 30% 30%, var(--label-light), var(--label-mid) 80%);
  }
  .bean-band {
    position: absolute;
    left: 0;
    width: 100%;
    height: 40px;
    background: linear-gradient(90deg, var(--bean-dark), var(--bean-mid) 20%, var(--bean-warm) 40%, var(--bean-mid) 60%, var(--bean-dark) 80%, var(--bean-mid));
  }
  .bean-band--top { top: 0; border-bottom: 6px solid #4a4a4e; }
  .bean-band--bottom { bottom: 0; border-top: 6px solid #4a4a4e; }

  .back-panel {
    position: absolute;
    left: 0;
    top: 46px;
    width: 390px;
    height: 340px;
    transform: rotate(180deg);
    font-family: "Special Elite", "Courier New", monospace;
    color: var(--ink);
    box-sizing: border-box;
    padding: 22px 22px 14px;
  }
  .pickup-line {
    font-size: 10.5px;
    line-height: 1.32;
    margin: 0 0 8px;
    text-align: justify;
  }
  .ingredients {
    margin: 14px auto 0;
    width: 270px;
    border: 1.5px solid var(--ink);
    padding: 7px 10px;
    font-size: 10px;
    line-height: 1.3;
    text-align: center;
  }
  .ingredients-title { display: block; margin-bottom: 2px; }
  .back-meta {
    position: absolute;
    left: 26px;
    right: 26px;
    bottom: 14px;
    display: flex;
    justify-content: space-between;
    font-size: 10.5px;
  }
  .fold-line {
    position: absolute;
    left: 0;
    top: 386px;
    width: 100%;
    height: 1px;
    background: #f4f4f6;
  }

  .model-photo {
    position: absolute;
    left: 0;
    top: 392px;
    width: 182px;
    height: 342px;
    background: linear-gradient(160deg, #3a2418 0%, var(--skin-light) 35%, var(--skin-dark) 70%, #8a4a2c 100%);
  }
  .brand-name {
    position: absolute;
    left: 186px;
    top: 404px;
    width: 200px;
    margin: 0;
    font-family: "Dancing Script", cursive;
    font-weight: 700;
    font-size: 44px;
    line-height: 1.05;
    color: var(--brand-brown);
    text-align: center;
  }
  .product-name {
    position: absolute;
    left: 196px;
    top: 584px;
    width: 180px;
    margin: 0;
    padding: 6px 0 4px;
    border-top: 2px solid var(--rule);
    border-bottom: 2px solid var(--rule);
    font-family: "Oswald", sans-serif;
    font-weight: 400;
    font-size: 25px;
    letter-spacing: 1px;
    color: #444;
    text-align: center;
  }
  .product-tagline {
    position: absolute;
    left: 192px;
    top: 640px;
    width: 190px;
    margin: 0;
    font-family: "Dancing Script", cursive;
    font-weight: 700;
    font-size: 17px;
    line-height: 1.2;
    color: var(--ink);
    text-align: center;
  }
</style>
</head>
<body>
  <div class="label">
    <div class="bean-band bean-band--top" role="img" aria-label="Band of roasted coffee beans"></div>

    <section class="back-panel">
      <p class="pickup-line">Hi babe! so you wanna get dirty! just show me the way to your bath. But first let me give you a proper introduction of myself. My name is rocco and I'm a coffee scrub wearing nothing but 250g of finest arabic coffee and sweet orange flavour and lots of other good stuff.</p>
      <p class="pickup-line">By the way I will help you with cellulite, stretch marks, psoriasis, varicose veins, eczema and acne. I'll smooth your lumps and bumps with brown sugar and sea salt, moisturise and tone your skin with cold pressed sweet almond oil, and use vitamins and minerals to work wonders from the outside in. Then I'll make us both smell good with a little orange essence.</p>
      <div class="ingredients">
        <span class="ingredients-title">INGREDIENTS:</span>
        Coffea Robusta Seed Powder (Coffee), Prunus Amygdalus Dulcis (Sweet Almond) Oil, Water (Aqua), Sodium Chloride (Salt), Sucrose (Brown Sugar). All ingredients organic.
      </div>
      <div class="back-meta">
        <span>NET WT. 200 g</span>
        <span>Best before date:</span>
      </div>
    </section>

    <div class="fold-line"></div>

    <div class="model-photo" role="img" aria-label="Photo of a woman with coffee scrub on her shoulders and back"></div>

    <h1 class="brand-name">Rocco<br>Velvetine</h1>
    <h2 class="product-name">COFFEE SCRUB</h2>
    <p class="product-tagline">Body peeling made of coffee, himalayan salt and additives</p>

    <div class="bean-band bean-band--bottom" role="img" aria-label="Band of roasted coffee beans"></div>
  </div>
</body>
</html>
```